New business card, letter head, email signature and Portfolio for our Security company.

We are an Elite security company that provides a top quality manpower services to protect high rise buildings, retail and all type of properties and would like a new business card/logo look.

- We would like the spot UV design.
- Matt black (double sided).
- We would like to incorporate a royal blue colour (feel free to experiment with it).
- Feel free to try different lengths with the card to make it stand out more than a normal business card.
- We would like the logo to be an eagle eye in the background (shines when card is tilted slightly in the background, either on the front, back or both sides of the card). Image attached as an example of eye shape (colour to be either black or royal blue).
- MAVRIN OAK GUARD PATROLS PTY. LTD. and MOGP to be placed on one side of the card and on the other side of the card to have;

- Name in slightly bigger font than the position (directly on the bottom on the name).
- Mobile number
- Email address
- Website email address
- PO BOX address

Can we please have the files in a format that we can edit.

Reason: I need to consult my business partner with the designs so far and will make a decision from there.

Target Market(s)

Security Industry

Industry/Entity Type

Business

Contact Information for Business Card

- Mobile number
- Email address
- Website email address
- PO BOX address

Logo Text

MOGP and underneath the MOGP please add MAVRIN OAK GUARD PATROLS PTY. LTD.

Font styles to use
Other font styles liked:
• bold type font

Colors
0255a3
000000

Requirements
Must have
• We are an Elite security company that provides a top quality manpower services to protect high rise buildings, retail and all type of properties and would like a new business card/logo look.
• - We would like the spot UV design.
• - Matt black (double sided).
• - We would like to incorporate a royal blue colour (feel free to experiment with it).
• - Feel free to try different lengths with the card to make it stand out more than a normal business card.
• - We would like the logo to be an eagle eye in the background (shines when card is tilted slightly in the background, either on the front, back or both sides of the card). Image attached as an example of eye shape (colour to be either black or royal blue).
• - MAVRIN OAK GUARD PATROLS PTY. LTD. and MOGP to be placed on one side of the card and on the other side of the card to have;
• - Name in slightly bigger font than the position (directly on the bottom on the name).
• - Mobile number
• - Email address
• - Website email address
• - PO BOX address
• Can we please have the files in a format that we can edit.
Nice to have
• Feel free to try different lengths with the card to make it stand out more than a normal business card.
• Please find "URBAN JUNGLE" font attached and incorporate MOGP into the same style with building's inside the MOGP bold front also add MAVRIN into the bottom part of the S and follow on E - Elite on the bottom S - SECURITY on the bottom S - SERVICES on the bottom of each letter.
• other than that, I'll be happy with a bold modern font for the MOGP and MAVRIN OAK GUARD PATROLS in a bold and thinner font underneath.

```html
<!DOCTYPE html>
<html lang="en">
<head>
<meta charset="utf-8">
<title>MAVRIN OAK GUARD PATROLS – Business Card</title>
<link rel="stylesheet" href="https://fonts.googleapis.com/css2?family=Russo+One&family=Poppins:wght@300;400&display=swap">
<style>
  :root {
    --backdrop: #d9d7d3;
    --card-matte: #141414;
    --spot-gloss: #2a2a2a;
    --spot-gloss-edge: #1a1a1a;
    --ink-light: #f2f2f0;
    --royal-blue: #0255a3;
    --royal-blue-bright: #2f7fd0;
    --ink-soft: #cfcfcc;
    --card-shadow: rgba(0, 0, 0, 0.28);
  }
  * { box-sizing: border-box; margin: 0; padding: 0; }
  html, body {
    width: 1200px;
    height: 918px;
    overflow: hidden;
    background: var(--backdrop);
  }
  .canvas {
    width: 1200px;
    height: 918px;
    display: flex;
    flex-direction: column;
    align-items: center;
    justify-content: center;
    gap: 40px;
  }
  .card {
    position: relative;
    width: 700px;
    height: 400px;
    background: var(--card-matte);
    box-shadow: 0 8px 22px var(--card-shadow);
    overflow: hidden;
  }

  .spot-uv-eye {
    position: absolute;
    border-radius: 50%;
    background: radial-gradient(ellipse at center, var(--spot-gloss) 0%, var(--spot-gloss-edge) 55%, var(--card-matte) 75%);
  }
  .card--front .spot-uv-eye { left: 110px; top: 60px; width: 480px; height: 280px; }
  .card--back .spot-uv-eye { left: 330px; top: -40px; width: 420px; height: 240px; }

  .wordmark {
    position: absolute;
    font-family: "Russo One", sans-serif;
    color: var(--ink-light);
    text-transform: uppercase;
    line-height: 1;
  }
  .wordmark__initials { display: block; }
  .wordmark__name { display: block; letter-spacing: 0.02em; }

  .card--front .wordmark {
    left: 50%;
    top: 50%;
    transform: translate(-50%, -50%);
    text-align: center;
    white-space: nowrap;
  }
  .card--front .wordmark__initials { font-size: 150px; letter-spacing: 0.01em; }
  .card--front .wordmark__name { font-size: 21px; margin-top: 12px; }

  .card--back .wordmark { left: 60px; top: 48px; white-space: nowrap; }
  .card--back .wordmark__initials { font-size: 96px; }
  .card--back .wordmark__name { font-size: 14px; margin-top: 8px; }

  .contact {
    position: absolute;
    right: 52px;
    bottom: 40px;
    text-align: right;
  }
  .contact__name {
    font-family: "Russo One", sans-serif;
    font-size: 34px;
    color: var(--royal-blue-bright);
    line-height: 1;
  }
  .contact__position {
    font-family: "Russo One", sans-serif;
    font-size: 15px;
    color: var(--ink-light);
    margin-top: 4px;
    margin-bottom: 14px;
  }
  .contact__line {
    font-family: "Poppins", sans-serif;
    font-weight: 300;
    font-size: 17px;
    color: var(--ink-soft);
    line-height: 1.5;
    text-align: left;
    width: 175px;
    margin-left: auto;
  }
  .contact__line--phone { text-align: right; }
</style>
</head>
<body>
<main class="canvas">
  <section class="card card--front" aria-label="Card front">
    <div class="spot-uv-eye" role="img" aria-label="Spot UV eagle eye background"></div>
    <div class="wordmark">
      <span class="wordmark__initials">MOGP</span>
      <span class="wordmark__name">Mavrin Oak Guard Patrols Pty. Ltd.</span>
    </div>
  </section>

  <section class="card card--back" aria-label="Card back">
    <div class="spot-uv-eye" role="img" aria-label="Spot UV eagle eye background"></div>
    <div class="wordmark">
      <span class="wordmark__initials">MOGP</span>
      <span class="wordmark__name">Mavrin Oak Guard Patrols Pty. Ltd.</span>
    </div>
    <div class="contact">
      <p class="contact__name">JOHN DOE</p>
      <p class="contact__position">POSITION</p>
      <p class="contact__line contact__line--phone">09XXXXXXXXX</p>
      <p class="contact__line">XXXX@email.com</p>
      <p class="contact__line">XXXX@email.com</p>
      <p class="contact__line">PO BOX Address</p>
    </div>
  </section>
</main>
</body>
</html>
```